Morrow Interiors

Hi, can you please make this design up for me. Morrow interiors text to front and Beatrice Morrow text to back in black. Small love hearts to be black. Mobile number to front text and back mobile number and email address text to be white. Open to your input 🙂 Thanks in advance! Beatrice

Industry/Entity Type

Interior Design

Colors

Designer to choose only greyscale colors for use in the design.

Requirements
Must have
• Little love hearts for dot on i

```html
<!DOCTYPE html>
<html lang="en">
<head>
<meta charset="utf-8">
<title>Morrow Interiors – Business Card</title>
<link rel="stylesheet" href="https://fonts.googleapis.com/css2?family=Montserrat:wght@300;400&display=swap">
<style>
  :root {
    --backdrop: #1d1d1d;
    --card-dark: #0f0f10;
    --card-light: #ffffff;
    --ink: #111111;
    --ink-soft: #6f6f72;
    --grey-band: #98999c;
    --silver: #c9c9cb;
    --rule: #8a8a8a;
  }
  * { margin: 0; padding: 0; box-sizing: border-box; }
  html, body {
    width: 1200px; height: 900px; overflow: hidden;
    background: var(--backdrop);
    font-family: "Montserrat", Arial, sans-serif;
  }
  .stage {
    width: 1200px; height: 900px;
    display: flex; flex-direction: column;
    align-items: center; justify-content: center; gap: 28px;
  }
  .card {
    width: 680px; height: 388px; position: relative; overflow: hidden;
  }
  .card--front { background: var(--card-dark); }
  .card--back { background: var(--card-light); }

  .wordmark {
    display: flex; align-items: center; gap: 14px;
    font-weight: 300; letter-spacing: 0.06em;
  }
  .wordmark__dot {
    width: 34px; height: 34px; border-radius: 50%;
  }
  .card--front .wordmark {
    position: absolute; left: 50%; top: 50%;
    transform: translate(-50%, -50%);
    font-size: 34px; color: var(--silver);
  }
  .card--front .wordmark__dot { background: var(--silver); }

  .card--back .wordmark {
    position: absolute; left: 40px; top: 34px;
    font-size: 24px; color: var(--ink-soft); gap: 10px;
  }
  .card--back .wordmark__dot { width: 26px; height: 26px; background: var(--ink); }

  .identity {
    position: absolute; left: 58px; top: 150px; width: 300px;
  }
  .identity__name {
    font-size: 24px; font-weight: 300; letter-spacing: 0.12em;
    color: var(--ink);
  }
  .identity__role {
    font-size: 15px; font-weight: 300; color: var(--ink-soft);
    margin-top: 2px; padding-bottom: 24px;
    border-bottom: 1.5px solid var(--rule);
  }

  .contacts {
    position: absolute; left: 58px; top: 268px; list-style: none;
  }
  .contacts__item {
    display: flex; align-items: center; gap: 10px;
    font-size: 16.5px; font-weight: 300; color: var(--ink-soft);
    line-height: 28px;
  }
  .contacts__icon { width: 17px; height: 17px; flex: none; }

  .accent-bands {
    position: absolute; inset: 0; width: 100%; height: 100%;
  }
</style>
</head>
<body>
<main class="stage">
  <section class="card card--front" aria-label="Card front">
    <div class="wordmark">
      <span class="wordmark__dot"></span>
      <span class="wordmark__name">Morrow Interiors</span>
    </div>
  </section>

  <section class="card card--back" aria-label="Card back">
    <svg class="accent-bands" viewBox="0 0 680 388" aria-hidden="true">
      <polygon points="680,160 680,275 545,388 410,388" fill="#111111"/>
      <polygon points="680,300 680,388 575,388" fill="#98999c"/>
    </svg>

    <div class="wordmark">
      <span class="wordmark__dot"></span>
      <span class="wordmark__name">Morrow Interiors</span>
    </div>

    <div class="identity">
      <h1 class="identity__name">BEATRICE MORROW</h1>
      <p class="identity__role">CEO &amp; Founder</p>
    </div>

    <ul class="contacts">
      <li class="contacts__item">
        <svg class="contacts__icon" viewBox="0 0 24 24" fill="none" stroke="#6f6f72" stroke-width="1.6">
          <circle cx="12" cy="12" r="10"/>
          <path d="M8.5 7.5l1.8-.4 1 2.4-1.2 1a7 7 0 003.4 3.4l1-1.2 2.4 1-.4 1.8c-4.8.4-8.4-3.2-8-8z"/>
        </svg>
        <span>+34 612.580.936</span>
      </li>
      <li class="contacts__item">
        <svg class="contacts__icon" viewBox="0 0 24 24" fill="none" stroke="#6f6f72" stroke-width="1.6">
          <rect x="2.5" y="5" width="19" height="14" rx="1"/>
          <path d="M3 6l9 7 9-7"/>
        </svg>
        <span>hello@morrowstudio.com</span>
      </li>
      <li class="contacts__item">
        <svg class="contacts__icon" viewBox="0 0 24 24" fill="none" stroke="#6f6f72" stroke-width="1.6">
          <circle cx="12" cy="12" r="10"/>
          <path d="M2 12h20M12 2c3 3 3 17 0 20M12 2c-3 3-3 17 0 20"/>
        </svg>
        <span>www.morrowstudio.com</span>
      </li>
    </ul>
  </section>
</main>
</body>
</html>
```